Marcus Lindqvist Photography needs a business card designs

I am looking for a business card with a logo clean and simple which I can use that logo on my website or on my pictures. It has to be very classy and very professional. Please look at my website at www.marcuslvqphoto.com for my signature. I'm thinking of something like that for my signature/logo. I'm still working on my website but you get an idea. I'm open to any design but not too busy graphics.

I will be printing the business card from qrivel.com.

Surprise me :)

contact me if you have any questions.

-ML

I'm receiving a lot of black background at the moment. I know my website is all black doesn't mean I want my card to be all black. Please send in with some white background as well. Thanks :)

check out some business cards that I found online. I think they are simple and look really awesome. I don't want a card that is too busy.

http://www.marcuslvqphoto.com/p270092084

Reason: Please extend the date for me. I haven't really receive any good design yet.

Printing

• -a logo that related to my first and last initial of my name "ML"
-double sided
• -I don't want my background to be all black.
-no pictures on the card

```html
<!DOCTYPE html>
<html lang="en">
<head>
<meta charset="utf-8">
<title>Marcus Lindqvist Photography – Business Card</title>
<link rel="stylesheet" href="https://fonts.googleapis.com/css2?family=Arimo:wght@400;700&display=swap">
<style>
  :root {
    --stage: #1a1c1e;
    --teal-light: #3fa3bf;
    --teal-mid: #1d6c84;
    --teal-deep: #0b3040;
    --ink: #050708;
    --ink-soft: #0d1418;
  }
  * { box-sizing: border-box; margin: 0; padding: 0; }
  html, body {
    width: 1200px; height: 800px; overflow: hidden;
    background: var(--stage);
    font-family: "Arimo", Arial, sans-serif;
  }
  .canvas { position: relative; width: 1200px; height: 800px; }

  .card {
    position: absolute; width: 560px; height: 330px; overflow: hidden;
    box-shadow: 0 12px 30px rgba(0,0,0,.55);
  }
  .card--front { left: 40px; top: 90px; }
  .card--back  { left: 600px; top: 380px; }

  .card__texture {
    position: absolute; inset: 0;
    background:
      radial-gradient(ellipse at 55% 45%, rgba(90,190,215,.45) 0%, rgba(0,0,0,0) 55%),
      linear-gradient(90deg, var(--teal-mid) 0%, var(--teal-light) 45%, var(--teal-mid) 75%, var(--teal-deep) 100%);
  }
  .card__texture::after {
    content: ""; position: absolute; inset: 0;
    background: radial-gradient(ellipse at center, rgba(0,0,0,0) 55%, rgba(0,0,0,.55) 100%);
  }

  .band { position: absolute; background: var(--ink); }

  /* front */
  .front__band-top    { left: 0; right: 0; top: 52px; height: 26px; }
  .front__band-bottom { left: 240px; right: 0; top: 192px; height: 26px; }
  .logo {
    position: absolute; left: 40px; top: 112px;
    display: flex; align-items: center; gap: 14px;
  }
  .logo__mark { width: 62px; height: 62px; background: var(--ink); }
  .logo__name {
    font-weight: 700; font-size: 30px; line-height: 1.05; color: var(--ink);
    letter-spacing: -0.5px;
  }
  .front__signature {
    position: absolute; right: 26px; top: 224px;
    font-weight: 700; font-size: 15px; color: var(--ink); letter-spacing: -0.3px;
  }

  /* back */
  .back__band-top    { left: 180px; right: 0; top: 26px; height: 22px; }
  .back__band-mid    { left: 0; right: 0; top: 188px; height: 28px; }
  .back__band-bottom { left: 0; right: 0; top: 252px; height: 22px; }
  .back__studio {
    position: absolute; left: 40px; top: 58px;
    font-weight: 700; font-size: 26px; color: var(--ink); letter-spacing: -0.5px;
  }
  .back__contact {
    position: absolute; left: 40px; top: 92px; list-style: none;
    font-size: 13px; line-height: 16px; color: var(--ink-soft);
  }
  .back__person {
    position: absolute; right: 50px; top: 142px; text-align: left;
    color: var(--ink);
  }
  .back__person-name { font-weight: 700; font-size: 20px; letter-spacing: -0.4px; line-height: 1; }
  .back__person-role { font-size: 13px; line-height: 1.2; }
</style>
</head>
<body>
<main class="canvas">

  <section class="card card--front" aria-label="Business card front">
    <div class="card__texture" role="img" aria-label="Teal weathered wood-grain texture"></div>
    <div class="band front__band-top"></div>
    <div class="band front__band-bottom"></div>
    <div class="logo">
      <span class="logo__mark"></span>
      <span class="logo__name">Marcus Lindqvist<br>Photography</span>
    </div>
    <p class="front__signature">Marcus Lindqvist</p>
  </section>

  <section class="card card--back" aria-label="Business card back">
    <div class="card__texture" role="img" aria-label="Teal weathered wood-grain texture"></div>
    <div class="band back__band-top"></div>
    <div class="band back__band-mid"></div>
    <div class="band back__band-bottom"></div>
    <h1 class="back__studio">ML Photography</h1>
    <ul class="back__contact">
      <li>marcus@marcuslvqphoto.com</li>
      <li>www.marcuslvqphoto.com</li>
      <li>P:555-014-2286</li>
    </ul>
    <div class="back__person">
      <p class="back__person-name">Marcus Lindqvist</p>
      <p class="back__person-role">Photographer</p>
    </div>
  </section>

</main>
</body>
</html>
```